NEW Wordpress Website Design for a Dynamic Long Term Healthcare Company in Hawaii

I would like a new website design for my current company, Marlow Haven Partners, which has two different brands - Marlow Homecare and Marlow Senior Living. You can see the current website at www.marlowhaven.example. The website should be built using Wordpress Software and the Elementor theme. The website should have a local Hawaii island/tropical feel, but look professional for healthcare. I'm looking for something fresh, and want the designer to select colors, styles, etc.

In the Header, on all pages, I would like a menu that includes Home Care, Senior Living, Rates, and About Us.
Under each of the Header Menu Titles, I would like these drop downs included:
Home Care (drop down pages)- Nurse Aide Care, 24-Hour Home Care, Skilled Nursing, Lifestyle Aide, Hospice at Home, Bathing & Meal Service.
Senior Living (drop down pages) - Long-Term Stay, Short-Term Stay.
Rates (drop down page) - Rates.
About Us (drop down pages) - Our Mission, Ohana Talk, About Doreen Marlow.

In the footer, on all pages, you should include the address: 248 Lanakila Ave, Suite 310, Honolulu, HI 96817. Phone number: 808-555-0173
The footer should also include buttons for a page called Learn, Caregiver Jobs, and each of the service page links to include: Nurse Aide Care, 24-Hour Home Care, Skilled Nursing, Lifestyle Aide, Hospice at Home, Bathing & Meal Service.
Please don't take the current website and redesign a few aspects. I'm looking for a completely different look and feel.

Target Market(s)

40-80 year olds

Industry/Entity Type

Long Term Healthcare

Coding

Coded - Design and coding required

Requirements
Should not have
• Our existing website as a template. We are looking for a complete redesign. Thank you.

```html
<!DOCTYPE html>
<html lang="en">
<head>
<meta charset="utf-8">
<title>Marlow Haven Partners — Homecare &amp; Senior Living</title>
<link href="https://fonts.googleapis.com/css2?family=Figtree:wght@400;500;600;700&display=swap" rel="stylesheet">
<style>
:root{
  --teal:#4f9a94;
  --teal-soft:#e3efed;
  --teal-line:#a9d0cb;
  --coral:#f3766c;
  --coral-soft:#fdf3f2;
  --ink:#161616;
  --text:#4a4a4a;
  --muted:#777;
  --panel:#edf3f2;
  --white:#fff;
  --black:#0b0b0b;
}
*{box-sizing:border-box;margin:0;padding:0}
html,body{width:1200px;height:3743px;overflow:hidden}
body{position:relative;font-family:"Figtree",Arial,sans-serif;color:var(--ink);background:var(--white)}
.abs{position:absolute}
.center{text-align:center;left:0;width:1200px}
.btn{position:absolute;display:flex;align-items:center;justify-content:center;border-radius:16px;font-size:11.5px;font-weight:600;color:#fff;text-decoration:none}
.btn-teal{background:var(--teal)}
.btn-coral{background:var(--coral)}
.btn-dark{background:var(--ink);border-radius:18px;font-size:12px}
.eyebrow{font-size:13px;font-weight:500;color:var(--teal)}
.section-title{font-size:31px;font-weight:400;line-height:40px;color:var(--ink)}
.wordmark{font-weight:600;color:var(--ink);text-align:center;line-height:1.1}

/* header */
.site-header{position:absolute;top:0;left:0;width:1200px;height:75px;background:rgba(255,255,255,.93);z-index:5}
.site-header .brand{left:86px;top:23px;width:110px;font-size:13px}
.nav{position:absolute;top:0;height:75px;display:flex;align-items:center;font-size:11.5px;color:var(--ink)}
.nav span{position:absolute;white-space:nowrap}
.caret{font-size:8px;margin-left:4px}
.phone-link{position:absolute;left:830px;top:28px;font-size:11.5px;display:flex;align-items:center;gap:8px}

/* hero */
.hero-photo{top:0;left:0;width:1200px;height:700px;background:linear-gradient(135deg,#7a5a3c 0%,#a98862 35%,#3e7aa8 60%,#6f8f6a 100%)}
.hero-title{top:210px;font-size:42px;font-weight:500;color:#fff;line-height:49px}
.hero-sub{top:322px;font-size:19.5px;color:#fff;line-height:25px}
.badge-text{font-size:16px}

/* about */
.about-bg{top:700px;left:0;width:1200px;height:420px;background:linear-gradient(180deg,#f7f7f7,#f2f2f2)}
.about-copy{left:199px;top:847px;width:390px;font-size:9.6px;line-height:15px;color:var(--text)}
.about-copy p+p{margin-top:11px}
.about-photo{left:690px;top:699px;width:312px;height:343px;border-radius:24px;background:linear-gradient(160deg,#5f8f3c,#a9c77a 55%,#eef0ea)}

/* service cards */
.card{position:absolute;width:250px;height:226px;background:#fff;border:1.5px solid var(--teal-line);box-shadow:3px 4px 0 var(--teal-soft);border-radius:3px;text-align:center}
.card.active{border-color:var(--coral);box-shadow:3px 5px 0 #f8b3ad}
.card .tab{position:absolute;left:100px;top:-1px;width:52px;height:48px;background:#eceeee;border-radius:0 0 26px 26px}
.card svg{position:absolute;left:100px;top:16px}
.card h3{position:absolute;top:88px;width:100%;font-size:15px;font-weight:500}
.card p{position:absolute;top:113px;left:22px;width:206px;font-size:9.6px;line-height:15px;color:var(--muted)}
.card .more{position:absolute;top:184px;width:100%;font-size:11px;font-weight:600;color:var(--teal)}
.card.active .more{color:var(--coral)}

/* senior living */
.living-panel{left:106px;top:1939px;width:988px;height:625px;background:var(--panel)}
.stay{top:2153px;height:275px;display:flex;align-items:center;justify-content:center;font-size:26px;font-weight:600;color:#fff}
.stay-long{left:0;width:587px;background:linear-gradient(120deg,#8a6a45,#c6b07a 45%,#6f7a88)}
.stay-short{left:612px;width:588px;background:linear-gradient(120deg,#6b4a36,#d8c9a8 50%,#3d8f9c)}

/* news */
.news-bg{top:2580px;left:0;width:1200px;height:1163px;background:linear-gradient(180deg,#fff 0%,var(--coral-soft) 12%)}
.news-img{position:absolute}
.news-cap{position:absolute;font-size:12px;line-height:16px;color:#333;text-align:center}

/* footer */
.footer-head{position:absolute;top:3490px;font-size:13px;font-weight:600;color:var(--coral)}
.footer-text{position:absolute;font-size:10.5px;color:#e6e6e6;line-height:16px}
.service-list{position:absolute;left:424px;top:3525px;font-size:10px;color:#e6e6e6;list-style:none}
.service-list li{height:22.7px}
.social{position:absolute;top:3584px;width:30px;height:30px;border-radius:50%;background:#2a2a2a}
.social.on{background:var(--teal)}
.footer-rule{left:199px;top:3683px;width:802px;height:1px;background:#333}
.copyright{top:3706px;font-size:9.5px;color:#ccc}
.copyright b{font-weight:400;color:var(--coral)}
</style>
</head>
<body>

<div class="abs hero-photo" role="img" aria-label="Photo of a caregiver laughing with a senior woman on a leather sofa in a bright living room"></div>

<header class="site-header">
  <div class="abs wordmark brand">Marlow Haven<br>Partners</div>
  <nav class="nav">
    <span style="left:356px;color:var(--coral)">
      <svg width="10" height="10" viewBox="0 0 10 10"><path d="M1 5 L5 1 L9 5 V9 H1Z" fill="var(--coral)"/></svg>
    </span>
    <span style="left:397px">Home Care<b class="caret">▾</b></span>
    <span style="left:491px">Senior Living<b class="caret">▾</b></span>
    <span style="left:593px">Rates<b class="caret">▾</b></span>
    <span style="left:658px">About Us<b class="caret">▾</b></span>
    <span style="left:741px">Contact Us</span>
  </nav>
  <div class="phone-link">
    <svg width="18" height="18" viewBox="0 0 24 24"><path d="M6.6 10.8a15 15 0 0 0 6.6 6.6l2.2-2.2a1 1 0 0 1 1-.25 11.4 11.4 0 0 0 3.6.57 1 1 0 0 1 1 1V20a1 1 0 0 1-1 1A17 17 0 0 1 3 4a1 1 0 0 1 1-1h3.5a1 1 0 0 1 1 1c0 1.25.2 2.45.57 3.6a1 1 0 0 1-.25 1z" fill="none" stroke="var(--coral)" stroke-width="1.6"/></svg>
    (808) 555-0173
  </div>
  <a class="btn btn-teal" style="left:962px;top:22px;width:131px;height:32px">Get a Free Quote</a>
</header>

<h1 class="abs center hero-title">Someone you can depend on...<br>Without question</h1>
<p class="abs center hero-sub">Marlow Senior Living, a beautiful adult residential care home, is located on the<br>windward side of oahu in kailua.</p>
<a class="btn btn-coral" style="left:535px;top:394px;width:130px;height:29px">Get a Free Quote</a>

<svg class="abs" style="left:0;top:440px" width="1200" height="270" viewBox="0 440 1200 270">
  <path d="M0 515 C90 540 160 545 215 538 L325 528 C420 565 520 610 600 665 C680 610 780 565 875 528 L985 538 C1040 545 1110 540 1200 515 V710 H0Z" fill="#f7f7f7"/>
  <path d="M0 528 C90 553 160 558 215 551 L325 541 C420 578 520 622 600 676 C680 622 780 578 875 541 L985 551 C1040 558 1110 553 1200 528" fill="none" stroke="var(--coral)" stroke-width="9"/>
  <circle cx="262" cy="528" r="64" fill="#fff"/>
  <circle cx="937" cy="528" r="64" fill="#fff"/>
</svg>
<div class="abs wordmark badge-text" style="left:207px;top:510px;width:110px">Marlow<br>Homecare</div>
<div class="abs wordmark badge-text" style="left:882px;top:510px;width:110px;color:var(--teal)">Marlow<br>Senior Living</div>

<div class="abs about-bg"></div>
<div class="abs eyebrow" style="left:199px;top:717px;font-size:12px">About us</div>
<h2 class="abs section-title" style="left:199px;top:746px;font-size:30px;line-height:38px">Hawaii's choice<br>Homecare &amp; Senior living</h2>
<div class="abs about-copy">
  <p>At Marlow Haven Partners, our mission is to provide compassionate and professional long-term healthcare services that empower individuals to maintain their highest level of independence, health, and well-being in the comfort of their own homes or ours, either through our licensed home healthcare agency - Marlow Homecare, or in our Adult Residential Care Home - Marlow Senior Living.</p>
  <p>We are dedicated to delivering personalized care that addresses the unique needs of each client, fostering a sense of trust, respect, and dignity ...</p>
</div>
<a class="btn btn-dark" style="left:199px;top:988px;width:137px;height:36px">Discover More</a>
<div class="abs about-photo" role="img" aria-label="Photo of a smiling senior couple in a tropical garden with palm leaves"></div>

<div class="abs center eyebrow" style="top:1197px">Home Care</div>
<h2 class="abs center section-title" style="top:1225px">Marlow Haven Partners provides a variety of professional<br>in-home health care services</h2>

<div class="card" style="left:200px;top:1326px">
  <div class="tab"></div>
  <svg width="52" height="52" viewBox="0 0 52 52"><circle cx="26" cy="20" r="8" fill="none" stroke="#333" stroke-width="1.6"/><path d="M12 46c0-9 6-15 14-15s14 6 14 15" fill="none" stroke="#333" stroke-width="1.6"/><circle cx="36" cy="40" r="5" fill="var(--coral)"/></svg>
  <h3>Nurse Aide Care</h3>
  <p>Lorem ipsum is simply dummy text of the printing and typesetting industry. lorem ipsum has been the industry's standard dummy remaining essentially...</p>
  <div class="more">Read more ↗</div>
</div>
<div class="card active" style="left:475px;top:1326px">
  <div class="tab"></div>
  <svg width="52" height="52" viewBox="0 0 52 52"><path d="M6 24 L26 6 L46 24 M11 20 V46 H41 V20" fill="none" stroke="#333" stroke-width="1.6"/><path d="M26 38c-6-4-9-7-9-10a4.5 4.5 0 0 1 9-1 4.5 4.5 0 0 1 9 1c0 3-3 6-9 10z" fill="var(--coral)"/></svg>
  <h3>24-Hour Home Care</h3>
  <p>Lorem ipsum is simply dummy text of the printing and typesetting industry. lorem ipsum has been the industry's standard dummy remaining essentially...</p>
  <div class="more">Read more ↗</div>
</div>
<div class="card" style="left:750px;top:1326px">
  <div class="tab"></div>
  <svg width="52" height="52" viewBox="0 0 52 52"><circle cx="26" cy="17" r="8" fill="none" stroke="var(--coral)" stroke-width="1.8"/><path d="M12 46c0-9 6-15 14-15s14 6 14 15" fill="none" stroke="#333" stroke-width="1.6"/><path d="M23 39h6M26 36v6" stroke="var(--coral)" stroke-width="1.8"/></svg>
  <h3>Skilled Nursing</h3>
  <p>Lorem ipsum is simply dummy text of the printing and typesetting industry. lorem ipsum has been the industry's standard dummy remaining essentially...</p>
  <div class="more">Read more ↗</div>
</div>
<div class="card" style="left:200px;top:1576px">
  <div class="tab"></div>
  <svg width="52" height="52" viewBox="0 0 52 52"><path d="M26 42c-12-8-18-14-18-21a9 9 0 0 1 18-3 9 9 0 0 1 18 3c0 7-6 13-18 21z" fill="var(--coral)"/><path d="M8 30h36M12 25v10M40 25v10" stroke="#333" stroke-width="2"/></svg>
  <h3>Lifestyle Aide</h3>
  <p>Lorem ipsum is simply dummy text of the printing and typesetting industry. lorem ipsum has been the industry's standard dummy remaining essentially...</p>
  <div class="more">Read more ↗</div>
</div>
<div class="card" style="left:475px;top:1576px">
  <div class="tab"></div>
  <svg width="52" height="52" viewBox="0 0 52 52"><circle cx="20" cy="38" r="9" fill="none" stroke="#333" stroke-width="1.6"/><circle cx="36" cy="10" r="4" fill="var(--coral)"/><path d="M34 16v18M34 22l-8 6M12 28h14" stroke="#333" stroke-width="1.6" fill="none"/></svg>
  <h3>Hospice at Home</h3>
  <p>Lorem ipsum is simply dummy text of the printing and typesetting industry. lorem ipsum has been the industry's standard dummy remaining essentially...</p>
  <div class="more">Read more ↗</div>
</div>
<div class="card" style="left:750px;top:1576px">
  <div class="tab"></div>
  <svg width="52" height="52" viewBox="0 0 52 52"><path d="M8 8v14a3 3 0 0 0 6 0V8M11 8v38M18 8v38" stroke="#333" stroke-width="1.6" fill="none"/><circle cx="34" cy="26" r="13" fill="none" stroke="var(--coral)" stroke-width="1.8"/><circle cx="34" cy="26" r="6" fill="var(--coral)"/></svg>
  <h3>Bathing &amp; Meal Service</h3>
  <p>Lorem ipsum is simply dummy text of the printing and typesetting industry. lorem ipsum has been the industry's standard dummy remaining essentially...</p>
  <div class="more">Read more ↗</div>
</div>
<a class="btn btn-teal" style="left:535px;top:1835px;width:130px;height:29px">Get a Free Quote</a>

<div class="abs living-panel"></div>
<div class="abs center eyebrow" style="top:2017px">Senior Living</div>
<h2 class="abs center section-title" style="top:2044px">We understand that choosing the right<br>senior living facility</h2>
<div class="abs stay stay-long" role="img" aria-label="Photo of seniors exercising with hand weights alongside a caregiver in a living room">Long-Term Stay</div>
<div class="abs stay stay-short" role="img" aria-label="Photo of a caregiver helping a senior man sit on a bed in a residence bedroom">Short-Term Stay</div>
<a class="btn btn-coral" style="left:535px;top:2460px;width:130px;height:30px">Get a Free Quote</a>

<div class="abs news-bg"></div>
<div class="abs center eyebrow" style="top:2643px">Care News</div>
<h2 class="abs center section-title" style="top:2663px;font-size:30px">Learn recent articles</h2>
<div class="news-img" style="left:106px;top:2786px;width:275px;height:218px;background:linear-gradient(135deg,#8a3d2a,#d8c88a 55%,#6a4a3a)" role="img" aria-label="Photo of a caregiver serving a meal to a senior couple at a dining table"></div>
<div class="news-img" style="left:405px;top:2724px;width:389px;height:280px;background:linear-gradient(135deg,#6b4a30,#d9cf8e 45%,#5a9a8a)" role="img" aria-label="Photo of three women knitting together on a sofa in a sunny room"></div>
<div class="news-img" style="left:818px;top:2786px;width:275px;height:218px;background:linear-gradient(135deg,#b9c9d6,#d8c59a 55%,#3a7a8a)" role="img" aria-label="Photo of a tidy residence room with a reclining chair and medical supplies"></div>
<div class="news-cap" style="left:106px;top:3018px;width:275px">What to look for in a honolulu<br>homecare facility</div>
<div class="news-cap" style="left:405px;top:3018px;width:389px">Is it time to look at a retirement home<br>for your loved one?</div>
<div class="news-cap" style="left:818px;top:3018px;width:275px">Signs your loved one needs<br>medication services</div>
<a class="btn btn-teal" style="left:535px;top:3080px;width:130px;height:30px">Learn More News</a>

<div class="abs wordmark" style="left:520px;top:3234px;width:160px;font-size:18px">Marlow Haven<br>Partners</div>
<svg class="abs" style="left:0;top:3280px" width="1200" height="463" viewBox="0 3280 1200 463">
  <path d="M0 3415 C90 3392 160 3388 215 3392 L325 3382 C420 3355 520 3320 600 3300 C680 3320 780 3355 875 3382 L985 3392 C1040 3388 1110 3392 1200 3415 V3743 H0Z" fill="var(--black)"/>
  <path d="M0 3402 C90 3379 160 3375 215 3379 L325 3369 C420 3342 520 3305 566 3290 M634 3290 C680 3305 780 3342 875 3369 L985 3379 C1040 3375 1110 3379 1200 3402" fill="none" stroke="var(--coral)" stroke-width="9"/>
  <circle cx="262" cy="3400" r="64" fill="#fff"/>
  <circle cx="937" cy="3400" r="64" fill="#fff"/>
</svg>
<div class="abs wordmark badge-text" style="left:207px;top:3382px;width:110px">Marlow<br>Homecare</div>
<div class="abs wordmark badge-text" style="left:882px;top:3382px;width:110px;color:var(--teal)">Marlow<br>Senior Living</div>

<div class="footer-head" style="left:200px">Contact Us</div>
<div class="footer-text" style="left:200px;top:3528px;font-size:14px;display:flex;align-items:center;gap:5px">
  <svg width="10" height="10" viewBox="0 0 24 24"><path d="M6.6 10.8a15 15 0 0 0 6.6 6.6l2.2-2.2a1 1 0 0 1 1-.25 11.4 11.4 0 0 0 3.6.57 1 1 0 0 1 1 1V20a1 1 0 0 1-1 1A17 17 0 0 1 3 4a1 1 0 0 1 1-1h3.5a1 1 0 0 1 1 1c0 1.25.2 2.45.57 3.6a1 1 0 0 1-.25 1z" fill="var(--coral)"/></svg>
  (808) 555-0173
</div>
<svg class="abs" style="left:200px;top:3563px" width="8" height="10" viewBox="0 0 8 10"><path d="M4 10S0 5.5 0 3.5a4 4 0 0 1 8 0C8 5.5 4 10 4 10z" fill="var(--coral)"/></svg>
<div class="footer-text" style="left:214px;top:3561px;font-size:9.8px">248 Lanakila Ave, Suite 310,<br>Honolulu, HI 96817</div>
<svg class="abs" style="left:200px;top:3614px" width="10" height="8" viewBox="0 0 10 8"><rect width="10" height="8" rx="1" fill="var(--coral)"/><path d="M0 1l5 4 5-4" stroke="#000" fill="none"/></svg>
<div class="footer-text" style="left:214px;top:3610px;font-size:9.8px">info@marlowhaven.example</div>

<div class="footer-head" style="left:424px">Our Service</div>
<ul class="service-list">
  <li>Nurse Aide Care</li>
  <li>24-Hour Home Care</li>
  <li>Skilled Nursing</li>
  <li>Lifestyle Aide</li>
  <li>Hospice at Home</li>
  <li>Bathing &amp; Meal Service</li>
</ul>

<div class="footer-head" style="left:612px">Office Hours</div>
<div class="footer-text" style="left:612px;top:3525px;font-size:10px">Monday - Friday 8:30am - 5:30pm</div>
<div class="footer-head" style="left:612px;top:3558px">Follow Us</div>
<div class="social" style="left:613px"></div>
<div class="social on" style="left:650px"></div>
<div class="social" style="left:688px"></div>
<div class="social" style="left:726px"></div>

<a class="btn btn-teal" style="left:819px;top:3494px;width:181px;height:30px">Learn Care News</a>
<a class="btn btn-coral" style="left:819px;top:3538px;width:181px;height:29px">Caregiver Jobs</a>

<div class="abs footer-rule"></div>
<div class="abs center copyright">© 2024 <b>Marlow Haven Partners</b>. All Rights Reserved. &nbsp;&nbsp;&nbsp;|&nbsp;&nbsp;&nbsp; Privacy Policy</div>

</body>
</html>
```